Corporate Design für Apotheke
Zielgruppe
Gesundheitswesen, Apotheke Zielgruppe kranke Menschen aber auch 'shopper'.
Aufgabenstellung
Das alte Logo ist leider viel zu filigran. Bei verschiedenen Druck kommt es oft nicht raus. Früher war das Logo eckig, es wurde vor Jahren mal als rund modernisiert.
Bin aber offen für alles.
Apotheke sollte grundsätzlich mit den Werten Seriosität, Vertrauen , und in unserem Fall auch Exklusivität, Premium- Segment verbunden werden. Im Anhang unser altes Logo. Ich bin zum ersten mal hier und freue mich auf kreative Vorschläge

```html
<!DOCTYPE html>
<html lang="de">
<head>
<meta charset="utf-8">
<title>Talblick Apotheke – Geschäftsausstattung</title>
<link href="https://fonts.googleapis.com/css2?family=Jost:wght@400;500;700&family=Caveat:wght@400&display=swap" rel="stylesheet">
<style>
  :root{
    --bg:#dedede;
    --paper:#ffffff;
    --green-dark:#0e6b3b;
    --green:#2e9a45;
    --green-light:#57b253;
    --text:#3d3d3d;
    --white:#ffffff;
  }
  *{box-sizing:border-box;margin:0;padding:0}
  html,body{width:1200px;height:822px;overflow:hidden}
  body{background:var(--bg);font-family:"Jost",sans-serif;color:var(--text);position:relative}
  .script{font-family:"Caveat",cursive;color:var(--green)}

  /* name lockup: plain name with a plain circle beside it */
  .name-lockup{display:flex;align-items:center;gap:7px}
  .name-lockup__dot{flex:none;border-radius:50%;background:var(--green-dark)}
  .name-lockup__text{font-family:"Jost",sans-serif;font-weight:500;color:var(--green-dark);white-space:nowrap}

  /* letter sheets */
  .sheet-back{position:absolute;left:290px;top:94px;width:472px;height:664px;background:var(--green-dark)}
  .letterhead{position:absolute;left:250px;top:60px;width:470px;height:664px;background:var(--paper);font-size:6.6px;line-height:9.5px}
  .letterhead > *{position:absolute}
  .slogan{left:44px;top:56px;font-size:16px;line-height:20px}
  .letterhead .name-lockup{left:301px;top:68px}
  .letterhead .name-lockup__dot{width:14px;height:14px}
  .letterhead .name-lockup__text{font-size:14px;line-height:18px}
  .sender-line{left:49px;top:101px;color:var(--green);font-size:6.2px}
  .recipient{left:55px;top:123px;font-style:normal}
  .contact{left:301px;top:131px;color:var(--green)}
  .contact p{margin-bottom:6px}
  .contact dl{display:grid;grid-template-columns:auto 1fr;column-gap:4px}
  .contact dt{font-weight:700;color:var(--green-dark)}
  .fold-mark{left:4px;width:7px;height:1px;background:var(--green)}
  .subject{left:55px;top:233px;font-weight:700;font-size:7px}
  .body-copy{left:55px;top:262px;width:370px}
  .body-copy p{margin-bottom:9.5px}
  .closing{left:55px;top:443px}
  .closing p{margin-bottom:9.5px}
  .footer-band{left:0;top:624px;width:470px;height:40px;background:var(--green-light);color:var(--white);font-size:6.2px;line-height:9.5px;padding:10px 0 0 44px}

  /* buttons */
  .button{position:absolute;width:68px;height:68px;border-radius:50%}
  .button--light{left:996px;top:104px;background:radial-gradient(circle at 40% 35%,#5fc25a,var(--green))}
  .button--dark{left:996px;top:193px;background:radial-gradient(circle at 40% 35%,#1f8a4a,var(--green-dark))}

  /* business cards */
  .card{position:absolute;left:868px;width:198px;height:112px}
  .card--front{top:305px;background:var(--paper);display:flex;align-items:center;justify-content:center}
  .card--front .name-lockup__dot{width:14px;height:14px}
  .card--front .name-lockup__text{font-size:14px}
  .card--back{top:447px;height:116px;background:var(--green-light);color:var(--white);padding:16px 18px;font-size:6.2px;line-height:9px}
  .card--back .card__name{display:block;font-weight:500;font-size:11px;line-height:14px;padding-bottom:5px;border-bottom:1px solid var(--white);margin-bottom:9px}
  .card--back p{margin-bottom:6px}
  .card--back dl{display:grid;grid-template-columns:auto 1fr;column-gap:5px}
  .card--back dt{font-weight:700}
  .card--back .script{color:var(--white);font-size:10px;display:block;margin:5px 0 0 20px}
</style>
</head>
<body>
  <div class="sheet-back"></div>

  <article class="letterhead">
    <div class="slogan script">… Wir sind für Sie da!</div>

    <div class="name-lockup">
      <span class="name-lockup__dot"></span>
      <span class="name-lockup__text">Talblick Apotheke</span>
    </div>

    <div class="sender-line">Talblick Apotheke | Musterstraße 1 | 79000 Lindenau</div>

    <address class="recipient">
      Clara Berger<br>Musterstraße 1<br>01234 Musterstadt
    </address>

    <div class="contact">
      <p>Musterstraße 1 | 79000 Lindenau</p>
      <dl>
        <dt>Fon:</dt><dd>012 987 40 20</dd>
        <dt>Web:</dt><dd>talblick-apotheke.de</dd>
        <dt>Mail:</dt><dd>info@talblick-apotheke.de</dd>
      </dl>
    </div>

    <span class="fold-mark" style="top:236px"></span>
    <span class="fold-mark" style="top:332px"></span>
    <span class="fold-mark" style="top:470px"></span>

    <div class="subject">Rechnungslegung November 2019</div>

    <div class="body-copy">
      <p>Sehr geehrte Frau Berger,</p>
      <p>Is evelibusant adist, simpori tatias volorem reicabore, omnitas explaut erum re officipsam aut acipic te volut fugit, aut minum fugiandant verum vellaut quibusapelit omnistrumet alitat dolecea verfere mporem restio. At facietus, con nos invel et ant, conesto de imolum, te int.</p>
      <p>Ibuscita soluptius quid quo to qui ullaut desti cumet laut et adit esequis cipit, odis vitia ditias ariorpo rionsedi dolori voluptatus nectiis dolupta speles quatemolupta vent illabor ibusdan ditaepe rissum essum rest que duciduntures est vendi rem que nulles int quatquodis et modignis dolorem volori ullut et ad est rem quisincid quatur restemolupta sit labo. Ipsunt ut quiae et quiderupta sit ius.</p>
      <p>Tust et voloris non pro occus, sequiditio eum cullaci dolut restrum apelit, nonsecabo. Neque restrum hil eum ipiet debis doluptur remquam que si bero ipsunt, conectur sapit quibus sit qui ut volo beat.</p>
      <p>Cerum earcidem facepero vit, tem ent voloruntem es magnimillaut mi, to eatiunt emoloratium ut eaquis quodi am quuntibuscit minissi dolupta doloreh enietur aut quam nulliquibus explitiorem re prenda placcae essequam hilique etur as ut earum rerio. Ur sum ne volor autemque volori doloratus.</p>
    </div>

    <div class="closing">
      <p>Mit freundlichen Grüßen</p>
      <p>Ihr Team der Talblick Apotheke</p>
    </div>

    <footer class="footer-band">
      Talblick Apotheke | Inhaber Apotheker Paul Beispiel | USt-IdNr. DE 100 200 300 | Handelsregisternr. 10987654321<br>
      Mo – Fr 8.00 – 19.00 Uhr, Sa 10.00 – 14.00 Uhr | Bank XXXXXX | BIC XXXXXXXXXXX | IBAN DE53 2222 3333 4444 5555 66
    </footer>
  </article>

  <div class="button button--light"></div>
  <div class="button button--dark"></div>

  <section class="card card--front">
    <div class="name-lockup">
      <span class="name-lockup__dot"></span>
      <span class="name-lockup__text">Talblick Apotheke</span>
    </div>
  </section>

  <section class="card card--back">
    <span class="card__name">Talblick Apotheke</span>
    <p>Musterstraße 1 | 79000 Lindenau</p>
    <dl>
      <dt>Fon:</dt><dd>012 987 40 20</dd>
      <dt>Web:</dt><dd>talblick-apotheke.de</dd>
      <dt>Mail:</dt><dd>info@talblick-apotheke.de</dd>
    </dl>
    <span class="script">… Wir sind für Sie da!</span>
  </section>
</body>
</html>
```